Farming postcard

Postcards for subdivisions that I have sold houses and I want it in the form of a template so I can change the photos from eight sold properties. The front should be somewhat eye catching and grab the attention of a would-be home seller. Something along the lines of turning for sale into sold for the last 30 years in Northern Colorado.

Farming

```html
<!DOCTYPE html>
<html lang="en">
<head>
<meta charset="utf-8">
<title>Farming Postcard – Hearth Realty</title>
<link rel="stylesheet" href="https://fonts.googleapis.com/css2?family=Oswald:wght@400;500&family=Josefin+Sans:wght@300;400;600&display=swap">
<style>
  :root {
    --page-bg: #e9e9e9;
    --card-white: #ffffff;
    --brand-blue: #2f67b0;
    --brand-red: #a3201f;
    --sold-red: #d6262a;
    --text-blue: #2b5fa8;
    --photo-top: #2f7f9e;
    --photo-mid: #4d7d86;
    --photo-low: #6b5238;
    --photo-pool: #1f4a5c;
  }
  * { margin: 0; padding: 0; box-sizing: border-box; }
  html, body { width: 1200px; height: 855px; overflow: hidden; }
  body { background: var(--page-bg); position: relative; font-family: "Josefin Sans", sans-serif; }

  /* Front card */
  .card-front {
    position: absolute; left: 55px; top: 102px; width: 467px; height: 602px;
    background: var(--brand-blue); overflow: hidden;
  }
  .front-photo {
    position: absolute; left: 0; top: 0; width: 467px; height: 463px;
    background: linear-gradient(180deg, var(--photo-top) 0%, var(--photo-mid) 40%, var(--photo-low) 68%, var(--photo-pool) 100%);
  }
  .front-frame {
    position: absolute; left: 17px; top: 16px; width: 433px; height: 572px;
    border: 3px solid var(--card-white); border-radius: 8px;
  }
  .front-headline {
    position: absolute; left: 42px; top: 52px;
    font-family: "Oswald", sans-serif; font-weight: 500; font-size: 62px; line-height: 62px;
    color: var(--card-white); text-transform: uppercase; letter-spacing: -0.5px;
  }
  .sold-sign {
    position: absolute; left: 150px; top: 298px; width: 212px; height: 88px;
    background: var(--sold-red); transform: rotate(-15deg);
    display: flex; align-items: center; justify-content: center;
    font-family: "Josefin Sans", sans-serif; font-weight: 600; font-size: 66px; color: var(--card-white);
    padding-top: 10px; letter-spacing: 1px;
  }
  .front-call {
    position: absolute; left: 0; width: 467px; top: 472px; text-align: center;
    font-weight: 300; font-size: 17px; color: var(--card-white); text-transform: uppercase; letter-spacing: 0.5px;
  }
  .front-phone {
    position: absolute; left: 0; width: 467px; top: 488px; text-align: center;
    font-family: "Oswald", sans-serif; font-weight: 500; font-size: 42px; color: var(--card-white);
  }
  .brand-name {
    font-family: "Josefin Sans", sans-serif; font-weight: 600; color: var(--card-white);
    text-transform: uppercase; letter-spacing: 1px; display: flex; align-items: center; gap: 7px;
  }
  .brand-name .mark { width: 12px; height: 12px; background: var(--card-white); }
  .front-brand { position: absolute; left: 0; width: 467px; top: 558px; justify-content: center; font-size: 19px; }

  /* Back card */
  .card-back {
    position: absolute; left: 555px; top: 170px; width: 602px; height: 467px; background: var(--card-white);
  }
  .back-frame {
    position: absolute; left: 14px; top: 15px; width: 574px; height: 436px;
    border: 4px solid var(--brand-blue); border-radius: 9px;
  }
  .agent-panel {
    position: absolute; left: 18px; top: 18px; width: 273px; height: 277px; background: var(--brand-red);
  }
  .back-brand { position: absolute; left: 15px; top: 28px; font-size: 19px; }
  .tagline { position: absolute; left: 0; width: 273px; text-align: center; color: var(--card-white); font-weight: 300; text-transform: uppercase; white-space: nowrap; }
  .tagline-small { top: 98px; font-size: 23px; }
  .tagline-mid { top: 127px; font-size: 37px; }
  .tagline-big { top: 172px; font-size: 64px; }
  .agent-name {
    position: absolute; left: 113px; top: 277px; font-size: 19px; line-height: 19px; color: var(--card-white);
    font-weight: 400; letter-spacing: 0.5px; white-space: nowrap;
  }
  .agent-portrait {
    position: absolute; left: 18px; top: 260px; width: 82px; height: 125px;
    background: linear-gradient(180deg, #6f7d86 0%, #5a4a3e 55%, #2e2c2c 100%);
  }
  .agent-bio {
    position: absolute; left: 100px; top: 295px; width: 191px; height: 90px; background: var(--brand-blue);
    color: var(--card-white); font-size: 9.2px; line-height: 12px; padding: 9px 3px 0 13px; font-weight: 400;
  }
  .contact { position: absolute; left: 297px; top: 54px; color: var(--text-blue); font-weight: 300; }
  .contact-web { font-size: 11.5px; letter-spacing: 0.3px; text-transform: uppercase; }
  .contact-line { font-size: 19px; margin-top: 6px; }
  .contact-line .label { font-size: 10px; text-transform: uppercase; }
</style>
</head>
<body>
  <section class="card-front">
    <div class="front-photo" role="img" aria-label="Photo of a sold home at dusk with a lit terrace and pool"></div>
    <div class="front-frame"></div>
    <h1 class="front-headline">Increase<br>Your Homes<br>Value</h1>
    <div class="sold-sign">SOLD</div>
    <p class="front-call">Call to selling your home</p>
    <p class="front-phone">970-555-0142</p>
    <div class="brand-name front-brand"><span class="mark"></span>Hearth Realty</div>
  </section>

  <section class="card-back">
    <div class="back-frame"></div>
    <div class="agent-panel">
      <div class="brand-name back-brand"><span class="mark"></span>Hearth Realty</div>
      <p class="tagline tagline-small">Your Professional</p>
      <p class="tagline tagline-mid">Real Estate</p>
      <p class="tagline tagline-big">Seller</p>
    </div>
    <div class="agent-portrait" role="img" aria-label="Portrait photo of the agent"></div>
    <p class="agent-name">DAN HOLLISTER</p>
    <p class="agent-bio">24 years in the business &amp; still going strong. From Single Family Homes to Multimillion dollar Commercial properties &amp; everything in between. I would be honored to extend my services to you with your Real Estate needs.</p>
    <div class="contact">
      <p class="contact-web">www.hearthrealtyhomes.com</p>
      <p class="contact-line"><span class="label">Office:</span> 970-555-0187</p>
      <p class="contact-line"><span class="label">Cell:</span> 970-555-0142</p>
    </div>
  </section>
</body>
</html>
```